Career development coaching - school lever to adults, needs a business card

Tandel Grove - An independent Career Advice business that provides 1-2-1 advice,for career development, entrepreneurial support and workshops needs a business card. Our clients of all ages (school leaver to adults looking for a career move) and universities and colleges. We would like the card to be double-sided with a modern, professional look. Looking for something professional yet very creative and original. Want a standard size business card that inspires a second look because it stands out from the rest.

One side of the card to have a design incorporating the logo with Tandel Grove name with the strap line “Helping you find your future” and space for the company website

Other side of the card to the logo/Tandel Grove name and the usual contact information:
Individual Name
Job Title (for example, Director)
Phone number
Email address
Company website address

Facebook, LinkedIn and Twitter links will need to go somewhere (back or front!)

The design will be used for 3 individuals so should be editable so that we can update as needed/as we grow.

Attached is the company logo/colours to be incorporated.

Target Market(s)

1-2-1 advice,for career development, entrepreneurial support and workshops needs a business card. Our clients of all ages (school leaver to adults looking for a career move) and universities and colleges.

Industry/Entity Type

Consulting

Contact Information for Business Card

Individual Name
Phone number
Email address
Company website address

Font styles to use
Sans Serif

Colors
0255a3
3176b5
faa54b
f78f20
85acd3
cfdeed

Requirements
Must have
• use the Tandel Grove Logo in some way - using the colours and the blue/orange palette
• For the logo - hope this makes sense to someone or if they direclty relate to the logo image attached!
• For the Orange:- Pantone 1585 C
• In CMYK : C3 M71 Y100 K0
• For the Blue:- 100% Pantone 7469 C
• In CMYK : C100 M62 Y27 K7
• Please feel free to contact me with any questions for more info
Nice to have
• happy to see any creative designs
Should not have
• Nothing too traditional,

```html
<!DOCTYPE html>
<html lang="en">
<head>
<meta charset="utf-8">
<title>Tandel Grove – Business Card</title>
<link href="https://fonts.googleapis.com/css2?family=Montserrat:wght@500;600&family=Alice&display=swap" rel="stylesheet">
<style>
  :root {
    --page: #2b2b2c;
    --card-dark: #1c252b;
    --card-light: #35434c;
    --orange: #f78f20;
    --blue: #0255a3;
    --blue-soft: #3176b5;
    --tagline: #85acd3;
    --ink: #e8eef3;
  }
  * { margin: 0; padding: 0; box-sizing: border-box; }
  html, body { width: 1200px; height: 900px; overflow: hidden; }
  body {
    background: var(--page);
    font-family: "Montserrat", sans-serif;
    position: relative;
  }
  .card {
    position: absolute;
    left: 290px;
    width: 620px;
    height: 354px;
    background: radial-gradient(ellipse at 60% 25%, var(--card-light) 0%, var(--card-dark) 72%);
    box-shadow: 0 14px 40px rgba(0,0,0,.55);
    overflow: hidden;
  }
  .card--back { top: 60px; }
  .card--front { top: 476px; }

  .brand { position: absolute; display: flex; align-items: center; }
  .brand__mark { border-radius: 50%; background: var(--blue); flex: none; }
  .brand__text { display: flex; flex-direction: column; }
  .brand__name {
    font-weight: 600;
    color: var(--orange);
    text-transform: uppercase;
    letter-spacing: .06em;
    white-space: nowrap;
    line-height: 1.1;
  }
  .brand__tagline {
    font-family: "Alice", serif;
    color: var(--tagline);
    white-space: nowrap;
  }

  /* contact side */
  .card--back .brand { left: 40px; top: 212px; gap: 16px; }
  .card--back .brand__mark { width: 46px; height: 46px; }
  .card--back .brand__name { font-size: 23px; }
  .card--back .brand__tagline { font-size: 16px; margin-top: 4px; }

  .contact { position: absolute; left: 356px; top: 96px; width: 240px; height: 156px; }
  .contact__arcs { position: absolute; inset: 0; }
  .contact__body { position: absolute; left: 34px; top: 14px; color: var(--ink); }
  .contact__name { font-size: 14px; font-weight: 600; }
  .contact__role { font-size: 13px; font-weight: 500; opacity: .85; margin-bottom: 12px; }
  .contact__line { font-size: 12.5px; font-weight: 500; line-height: 1.6; opacity: .9; }

  /* brand side */
  .card--front .brand { left: 196px; top: 118px; gap: 22px; }
  .card--front .brand__mark { width: 82px; height: 82px; }
  .card--front .brand__name { font-size: 34px; }
  .card--front .brand__tagline { font-size: 22px; margin-top: 6px; }
  .website {
    position: absolute;
    right: 50px;
    bottom: 58px;
    font-family: "Alice", serif;
    font-size: 13px;
    letter-spacing: .12em;
    color: var(--ink);
  }
</style>
</head>
<body>

  <section class="card card--back" aria-label="Business card, contact side">
    <div class="brand">
      <span class="brand__mark"></span>
      <div class="brand__text">
        <span class="brand__name">Tandel Grove</span>
        <span class="brand__tagline">Helping you find your future</span>
      </div>
    </div>

    <div class="contact">
      <svg class="contact__arcs" viewBox="0 0 240 156" aria-hidden="true">
        <path d="M22 40 A54 54 0 0 0 22 116" fill="none" stroke="var(--blue-soft)" stroke-width="7" stroke-linecap="round"/>
        <path d="M218 40 A54 54 0 0 1 218 116" fill="none" stroke="var(--blue-soft)" stroke-width="7" stroke-linecap="round"/>
      </svg>
      <div class="contact__body">
        <p class="contact__name">Individual Name</p>
        <p class="contact__role">Director</p>
        <p class="contact__line">Ph: 555-0142-87</p>
        <p class="contact__line">E: info@tandelgrove.com</p>
        <p class="contact__line">W: tandelgrove.com</p>
      </div>
    </div>
  </section>

  <section class="card card--front" aria-label="Business card, brand side">
    <div class="brand">
      <span class="brand__mark"></span>
      <div class="brand__text">
        <span class="brand__name">Tandel Grove</span>
        <span class="brand__tagline">Helping you find your future</span>
      </div>
    </div>
    <p class="website">www.tandelgrove.com</p>
  </section>

</body>
</html>
```